Wedding Decor and Entertianment business card

Company - We run a weddings and events company called Amber Finch, we provide most entertainment and decor services to our customers.

Initial idea is ....
A simple business card with logo on the front, this will be spot varnish. On a matt black background.
The reverse will be simple contact information.

But happy to try things outside of the box and would welcome some crazy ideas.

Target Market(s)

wedding couples - 21 - 40
High end wedding venues.

Industry/Entity Type

Wedding

Contact Information for Business Card

01492 718 263
amberfinchevents.co.uk
rowan@amberfinchevents.co.uk
or
helena@amberfinchevents.co.uk

Requirements
Nice to have
• black matt background with spot varnish logo on the front.

```html
<!DOCTYPE html>
<html lang="en">
<head>
<meta charset="utf-8">
<title>Amber Finch – Business Card</title>
<link rel="stylesheet" href="https://fonts.googleapis.com/css2?family=Bebas+Neue&family=Open+Sans:wght@400&family=Josefin+Sans:wght@300&display=swap">
<style>
  :root {
    --backdrop: #6b4a35;
    --card: #262626;
    --accent: #8c5f8c;
    --ink: #f2f2f2;
    --varnish: #141414;
  }
  * { margin: 0; padding: 0; box-sizing: border-box; }
  html, body { width: 1200px; height: 1000px; overflow: hidden; }
  body { background: var(--backdrop); position: relative; font-family: "Open Sans", sans-serif; }

  .card {
    position: absolute;
    left: 266px;
    width: 665px;
    height: 397px;
    background: var(--card);
    border-radius: 22px;
  }
  .card--contact { top: 73px; }
  .card--brand { top: 533px; }

  .identity {
    position: absolute;
    right: 356px;
    top: 164px;
    text-align: right;
  }
  .identity__name {
    font-family: "Bebas Neue", sans-serif;
    font-size: 44px;
    line-height: 40px;
    color: var(--accent);
    letter-spacing: 0.5px;
  }
  .identity__role {
    font-size: 16px;
    line-height: 22px;
    color: var(--ink);
  }

  .divider {
    position: absolute;
    left: 331px;
    top: 167px;
    width: 2px;
    height: 58px;
    background: var(--ink);
  }

  .contact-list {
    position: absolute;
    left: 352px;
    top: 162px;
    list-style: none;
  }
  .contact-list__item {
    display: flex;
    align-items: center;
    height: 23.5px;
    font-size: 16px;
    color: var(--ink);
  }
  .contact-list__icon {
    width: 14px;
    height: 14px;
    margin-right: 10px;
    fill: var(--accent);
  }

  .brand {
    position: absolute;
    left: 0;
    right: 0;
    top: 176px;
    display: flex;
    justify-content: center;
    align-items: center;
    gap: 22px;
  }
  .brand__dot {
    width: 44px;
    height: 44px;
    border-radius: 50%;
    background: var(--varnish);
  }
  .brand__name {
    font-family: "Josefin Sans", sans-serif;
    font-weight: 300;
    font-size: 34px;
    letter-spacing: 9px;
    color: var(--varnish);
    text-transform: uppercase;
  }
</style>
</head>
<body>
  <section class="card card--contact">
    <div class="identity">
      <div class="identity__name">Noor Hale</div>
      <div class="identity__role">President</div>
    </div>
    <div class="divider"></div>
    <ul class="contact-list">
      <li class="contact-list__item">
        <svg class="contact-list__icon" viewBox="0 0 14 14" aria-hidden="true">
          <path d="M1 5c0-2 2-3 6-3s6 1 6 3v1h-3V4.5H4V6H1z"/>
          <rect x="3" y="7" width="8" height="5" rx="1"/>
        </svg>
        01492 718 263
      </li>
      <li class="contact-list__item">
        <svg class="contact-list__icon" viewBox="0 0 14 14" aria-hidden="true">
          <rect x="1" y="3" width="12" height="8" rx="1"/>
          <path d="M1.5 3.5 7 8l5.5-4.5" stroke="#262626" stroke-width="1.2" fill="none"/>
        </svg>
        helena@amberfinchevents.co.uk
      </li>
      <li class="contact-list__item">
        <svg class="contact-list__icon" viewBox="0 0 14 14" aria-hidden="true">
          <circle cx="7" cy="7" r="6"/>
          <path d="M7 1v12M1 7h12M3 3.5c2.5 1.5 5.5 1.5 8 0M3 10.5c2.5-1.5 5.5-1.5 8 0" stroke="#262626" stroke-width="1" fill="none"/>
        </svg>
        amberfinchevents.co.uk
      </li>
    </ul>
  </section>

  <section class="card card--brand">
    <div class="brand">
      <span class="brand__dot"></span>
      <span class="brand__name">Amber Finch</span>
    </div>
  </section>
</body>
</html>
```